Web Site Design and Business Card design for Recruiting Company

There are three major tasks in this project:
1) I need to re-design my newly created website www.talvenhire.net using the same logo but creating a totally different recruiting template that will apply better for a recruitment site. I want to use the elements of the Talvenhire Network logo (which is the road junction) and red, black and gray colors throughout the website. I need someone to both design and launch the site...
2) I would also like to design a double sided business card using the same logo/colors and elements as described above
3) I would also like to have a small thumbnail logo created. As our large logo cannot be previewed easily on the Corvanet or on Pellmark Orbit tab images

The design should be contemporary, minimalist and slick

```html
<!DOCTYPE html>
<html lang="en">
<head>
<meta charset="utf-8">
<title>Talvenhire Network</title>
<link rel="stylesheet" href="https://fonts.googleapis.com/css2?family=Lato:wght@400;700;900&display=swap">
<style>
:root{--red:#e0141e;--red-deep:#c50a12;--ink:#111;--dark:#1a1a1a;--gray:#efefef;--mid:#777;--white:#fff}
*{box-sizing:border-box;margin:0;padding:0}
html,body{width:1200px;height:2965px;overflow:hidden}
body{font-family:'Lato',sans-serif;color:var(--ink);background:var(--white);position:relative}
.abs{position:absolute}
.btn{position:absolute;display:flex;align-items:center;justify-content:center;border:2px solid currentColor;font-weight:700;text-transform:uppercase;font-size:17px}
/* header */
.header{left:0;top:0;width:1200px;height:105px;background:var(--white)}
.brand{left:173px;top:28px;display:flex;align-items:center;gap:8px;font-size:19px;font-weight:700;color:var(--ink)}
.brand-mark{width:14px;height:14px;background:var(--red)}
.nav a{position:absolute;top:36px;font-size:17px;font-weight:700;color:var(--ink);text-decoration:none;transform:translateX(-50%);white-space:nowrap}
.nav a.active{color:var(--red)}
.nav-bar{left:472px;top:100px;width:61px;height:5px;background:var(--red)}
/* hero */
.hero{left:0;top:105px;width:1200px;height:590px;background:linear-gradient(180deg,#bdbdbd 0%,#8a8a8a 45%,#3d3d3d 100%)}
.hero-badge{left:134px;top:213px;width:368px;height:368px;border-radius:50%;background:var(--red);color:var(--white);text-align:center}
.hero-badge h1{font-weight:400;font-size:36px;margin-top:92px;line-height:1.2}
.hero-badge h1 b{display:block;font-weight:700;font-size:36px}
.hero-badge p{font-size:18px;line-height:27px;margin-top:10px}
.hero-badge .btn{left:101px;top:249px;width:163px;height:50px;color:var(--white)}
/* about */
.about{left:0;top:695px;width:1200px;height:580px;background:linear-gradient(180deg,#e6e6e6 0%,#fafafa 40%,#fff 100%)}
.section-title{position:absolute;left:0;width:1200px;text-align:center;font-size:37px;font-weight:700}
.section-title .hl{color:var(--red)}
.rule{position:absolute;height:3px;width:74px;background:var(--ink)}
.about p{position:absolute;left:190px;width:820px;top:140px;text-align:center;font-size:19px;line-height:35px;color:#333}
/* services */
.svc{position:absolute;color:var(--white);text-align:center}
.svc h3{font-size:25px;font-weight:700;line-height:25px;text-transform:uppercase}
.svc ul{list-style:none;font-size:16px;line-height:31px;margin-top:14px}
.svc-side{top:1276px;height:447px;background:linear-gradient(135deg,#3a3a3a,#1d1d1d 60%,#2e2e2e)}
.svc-main{left:388px;top:1241px;width:404px;height:516px;background:linear-gradient(160deg,#f01a22,#d30d15 60%,#b40610)}
.svc .btn{color:var(--white);width:163px;height:50px}
.icon{display:block;margin:0 auto}
/* posts */
.posts{left:0;top:1757px;width:1200px;height:619px;background:var(--gray)}
.post{position:absolute;top:1910px;width:284px;height:363px;background:var(--white);border:2px solid #d4d4d4;padding:12px 10px}
.post-img{height:152px;width:100%}
.post h4{font-size:16px;font-weight:400;line-height:18px;margin:16px 15px 0;color:var(--dark)}
.post .meta{font-size:12px;font-weight:700;color:var(--red);margin:8px 15px 0}
.post p{font-size:12px;line-height:16px;color:var(--mid);margin:9px 15px 0}
.post .btn{left:25px;top:302px;width:112px;height:34px;font-size:12px;color:var(--red)}
.post .btn{color:var(--ink);border-color:var(--red)}
/* contact */
.contact{left:0;top:2376px;width:1200px;height:443px;background:#141414}
.field{position:absolute;border:2px solid #cfcfcf;color:#fff;font-size:14px;padding:12px 16px}
.submit{left:523px;top:2709px;width:154px;height:42px;background:var(--red);color:#fff;font-size:17px;font-weight:700;display:flex;align-items:center;justify-content:center}
/* footer */
.footer a{position:absolute;top:2862px;font-size:17px;font-weight:700;color:var(--ink);text-decoration:none}
.copy{left:173px;top:2903px;font-size:14px;color:#333}
.social{position:absolute;top:2850px;width:42px;height:42px;border-radius:50%;background:var(--red);color:#fff;font-size:11px;font-weight:700;display:flex;align-items:center;justify-content:center}
</style>
</head>
<body>

<header class="abs header">
  <div class="abs brand"><span class="brand-mark"></span>Talvenhire Network</div>
  <nav class="nav">
    <a class="active" style="left:502px">HOME</a>
    <a style="left:618px">ABOUT US</a>
    <a style="left:748px">SERVICES</a>
    <a style="left:888px">CONTACT US</a>
  </nav>
  <svg class="abs" style="left:983px;top:36px" width="22" height="22" viewBox="0 0 22 22"><circle cx="9" cy="9" r="6.5" fill="none" stroke="#999" stroke-width="2.5"/><line x1="14" y1="14" x2="20" y2="20" stroke="#999" stroke-width="2.5"/></svg>
  <div class="abs nav-bar"></div>
</header>

<section class="abs hero" role="img" aria-label="Black and white aerial photo of the Atlanta skyline and highway"></section>
<svg class="abs" style="left:64px;top:362px" width="30" height="60" viewBox="0 0 30 60"><polyline points="27,2 3,30 27,58" fill="none" stroke="#fff" stroke-width="2"/></svg>
<svg class="abs" style="left:1088px;top:362px" width="30" height="60" viewBox="0 0 30 60"><polyline points="3,2 27,30 3,58" fill="none" stroke="#fff" stroke-width="2"/></svg>
<div class="abs hero-badge">
  <h1>Welcome to<b>Talvenhire Network</b></h1>
  <p>Atlanta based talent advisory,<br>recruiting and staffing firm.</p>
  <span class="btn">Learn More</span>
</div>

<section class="abs about">
  <h2 class="section-title" style="top:68px">About <span class="hl">T</span>alvenhire Net<span class="hl">work</span></h2>
  <div class="rule" style="left:566px;top:122px"></div>
  <p>Talvenhire Network LLC is an Atlanta based talent advisory, recruiting and staffing firm. We help companies find skilled professionals within the shortest time frames though our unique network of business and personal connections nationwide and overseas.</p>
  <span class="btn" style="left:524px;top:269px;width:163px;height:50px;color:var(--red)">Learn More</span>
  <h2 class="section-title" style="top:455px">Our Services</h2>
  <div class="rule" style="left:561px;top:511px"></div>
</section>

<div class="svc svc-side" style="left:0;width:385px" role="img" aria-label="Photo of an IT professional at work">
  <svg class="icon" style="margin-top:26px" width="64" height="64" viewBox="0 0 64 64" fill="none" stroke="#fff" stroke-width="2.5"><circle cx="32" cy="32" r="7"/><circle cx="8" cy="8" r="5"/><circle cx="56" cy="8" r="5"/><circle cx="8" cy="56" r="5"/><circle cx="56" cy="56" r="5"/><line x1="12" y1="12" x2="27" y2="27"/><line x1="52" y1="12" x2="37" y2="27"/><line x1="12" y1="52" x2="27" y2="37"/><line x1="52" y1="52" x2="37" y2="37"/></svg>
  <h3 style="margin-top:14px">Information<br>Technology</h3>
  <ul><li>Project Management</li><li>Web and Application Development</li><li>Network Administration</li><li>System Engineering and Administration</li><li>Software Engineering</li></ul>
  <span class="btn" style="left:121px;top:354px">Learn More</span>
</div>

<div class="svc svc-main" role="img" aria-label="Red-tinted photo of a telecom engineer on a tower">
  <svg class="icon" style="margin-top:40px" width="68" height="64" viewBox="0 0 68 64" fill="none" stroke="#fff" stroke-width="2.5"><circle cx="34" cy="22" r="14"/><path d="M18 22a16 16 0 0 1 32 0"/><rect x="14" y="20" width="6" height="10" rx="2"/><rect x="48" y="20" width="6" height="10" rx="2"/><path d="M51 30q0 10-12 10h-4"/><path d="M6 62q4-18 28-18t28 18z"/></svg>
  <h3 style="margin-top:18px">Telecommunications</h3>
  <ul><li>Project Management</li><li>Construction Management</li><li>Site Acquisition</li><li>L&amp;A Installation and Civil Work</li><li>RF Engineering and Network Design</li><li>Cell Site Integration</li></ul>
  <span class="btn" style="left:121px;top:385px">Learn More</span>
</div>

<div class="svc svc-side" style="left:797px;width:403px" role="img" aria-label="Photo of financial documents and charts on a desk">
  <svg class="icon" style="margin-top:26px" width="60" height="58" viewBox="0 0 60 58" fill="none" stroke="#fff" stroke-width="2.5"><rect x="2" y="2" width="56" height="40"/><line x1="30" y1="42" x2="30" y2="52"/><line x1="16" y1="55" x2="44" y2="55"/><rect x="14" y="24" width="6" height="12"/><rect x="24" y="16" width="6" height="20"/><rect x="34" y="12" width="6" height="24"/><rect x="44" y="22" width="5" height="14"/></svg>
  <h3 style="margin-top:16px">Accounting &amp;<br>Finance</h3>
  <ul><li>Financial Planning</li><li>Financial Management</li><li>Certified Public Accounting (CPA)</li><li>Audit</li><li>Cost Accounting</li></ul>
  <span class="btn" style="left:117px;top:345px">Learn More</span>
</div>

<section class="abs posts">
  <h2 class="abs" style="left:167px;top:70px;font-size:37px;font-weight:700">Recent Posts</h2>
  <div class="rule" style="left:169px;top:120px"></div>
</section>

<article class="post" style="left:162px">
  <div class="post-img" role="img" aria-label="Photo of a smiling businesswoman shaking hands" style="background:linear-gradient(135deg,#9a9a9a,#d8d8d8 50%,#6f6f6f)"></div>
  <h4>Duis non nunc Nulla rhoncus dictum metus Curabitur</h4>
  <div class="meta">By Author Name &nbsp;|&nbsp; JAN 20, 2019</div>
  <p>Duis non nunc Nulla rhoncus dictum metus Curabitur tristique mi condimen-tum orci Phasellus pellentesq</p>
  <span class="btn">Read More</span>
</article>
<article class="post" style="left:462px">
  <div class="post-img" role="img" aria-label="Photo of a smiling man in an office" style="background:linear-gradient(135deg,#7a5a46,#3b5148 50%,#8c8c8c)"></div>
  <h4>Duis non nunc Nulla rhoncus dictum metus Curabitur</h4>
  <div class="meta">By Author Name &nbsp;|&nbsp; JAN 20, 2019</div>
  <p>Duis non nunc Nulla rhoncus dictum metus Curabitur tristique mi condimen-tum orci Phasellus pellentesq</p>
  <span class="btn">Read More</span>
</article>
<article class="post" style="left:761px">
  <div class="post-img" role="img" aria-label="Photo of a hand touching a glowing people network graphic" style="background:linear-gradient(135deg,#2aa3a8,#1f4f6d 55%,#17384f)"></div>
  <h4>Duis non nunc Nulla rhoncus dictum metus Curabitur</h4>
  <div class="meta">By Author Name &nbsp;|&nbsp; JAN 20, 2019</div>
  <p>Duis non nunc Nulla rhoncus dictum metus Curabitur tristique mi condimen-tum orci Phasellus pellentesq</p>
  <span class="btn">Read More</span>
</article>

<section class="abs contact">
  <h2 class="section-title" style="top:52px;color:#fff">Contact Us</h2>
</section>
<div class="field" style="left:258px;top:2493px;width:337px;height:42px">First Name</div>
<div class="field" style="left:606px;top:2493px;width:338px;height:42px">Last Name</div>
<div class="field" style="left:258px;top:2543px;width:337px;height:42px">Email address</div>
<div class="field" style="left:606px;top:2543px;width:338px;height:42px">Phone Number</div>
<div class="field" style="left:258px;top:2597px;width:686px;height:92px">Type Message</div>
<div class="abs submit">SUBMIT</div>

<footer class="footer">
  <a style="left:173px">HOME</a>
  <a style="left:271px">ABOUT US</a>
  <a style="left:404px">SERVICES</a>
  <a style="left:532px">CONTACT US</a>
  <div class="abs copy">© 2019 Company Name &nbsp;All right reserved</div>
  <span class="social" style="left:830px" aria-label="Friendwall">Fw</span>
  <span class="social" style="left:880px" aria-label="Chirpline">Ch</span>
  <span class="social" style="left:929px" aria-label="Snapframe">Sf</span>
  <span class="social" style="left:979px" aria-label="Pinboardly">Pb</span>
</footer>

</body>
</html>
```